Visitenkarten-Design für Metzgerei
Zielgruppe
Metzgerei, Fleischsommelier
Zielgruppe: BBQ Szene
Aufgabenstellung
Visitenkarte gefalzt, Grundfarbe schwarz, mit unserem Logo, Foto sowie Sommelier-Logo
Standartangaben wie Internetadresse, Instagram,

```html
<!DOCTYPE html>
<html lang="de">
<head>
<meta charset="utf-8">
<title>Glutmeister – Visitenkarte gefalzt</title>
<link href="https://fonts.googleapis.com/css2?family=Montserrat:wght@400;600&display=swap" rel="stylesheet">
<style>
  :root {
    --stage: #c9ced0;
    --card-black: #0c0c0c;
    --card-charcoal: #2b2b2b;
    --gold: #f2c200;
    --white: #f2f2f2;
    --muted: #bdbdbd;
    --badge: #e3c06a;
    --badge-dark: #1a1a1a;
    --photo-deep: #141414;
    --photo-dark: #262626;
    --photo-mid: #5e5e5e;
    --photo-light: #8a8a8a;
  }
  * { box-sizing: border-box; margin: 0; padding: 0; }
  html, body { width: 867px; height: 1200px; overflow: hidden; }
  body {
    background: var(--stage);
    font-family: "Montserrat", sans-serif;
    color: var(--white);
    position: relative;
  }
  .spread {
    position: absolute;
    left: 63px;
    width: 740px;
    height: 250px;
    display: flex;
    box-shadow: 0 14px 30px rgba(0,0,0,.25);
  }
  .spread--outside { top: 200px; }
  .spread--inside { top: 700px; }
  .panel {
    position: relative;
    width: 370px;
    height: 250px;
    overflow: hidden;
  }
  .panel--charcoal { background: var(--card-charcoal); }
  .panel--black { background: var(--card-black); }

  /* Back panel: name and contacts */
  .contact {
    position: absolute;
    left: 36px;
    bottom: 30px;
  }
  .contact__name {
    font-size: 20px;
    font-weight: 600;
    letter-spacing: .3px;
    margin-bottom: 8px;
  }
  .contact__first { color: var(--gold); }
  .contact__last { color: var(--white); }
  .contact__line {
    font-size: 10px;
    line-height: 16px;
    color: var(--muted);
  }

  /* Front panel: wordmark */
  .wordmark {
    position: absolute;
    inset: 0;
    display: flex;
    align-items: center;
    justify-content: center;
    gap: 10px;
  }
  .wordmark__dot {
    width: 14px; height: 14px;
    border-radius: 50%;
    background: var(--gold);
  }
  .wordmark__name {
    font-size: 26px;
    font-weight: 600;
    color: var(--gold);
    letter-spacing: 1px;
  }

  /* Inside left: certificate badge as plain shape */
  .badge {
    position: absolute;
    left: 50%; top: 50%;
    width: 116px; height: 116px;
    margin: -58px 0 0 -58px;
    border-radius: 50%;
    background: var(--badge-dark);
    border: 4px solid var(--badge);
  }

  /* Inside right: portrait photo area */
  .photo {
    position: absolute;
    inset: 0;
    background:
      radial-gradient(ellipse 60% 55% at 62% 70%, var(--photo-light) 0%, var(--photo-mid) 35%, transparent 75%),
      radial-gradient(ellipse 45% 40% at 40% 20%, var(--photo-mid) 0%, transparent 80%),
      linear-gradient(160deg, var(--photo-deep) 0%, var(--photo-dark) 55%, var(--photo-deep) 100%);
  }
  .tagline {
    position: absolute;
    top: 22px;
    right: 26px;
  }
  .tagline__line {
    font-size: 9px;
    line-height: 13px;
    color: var(--white);
  }
</style>
</head>
<body>
  <section class="spread spread--outside" aria-label="Außenseite">
    <div class="panel panel--charcoal">
      <div class="contact">
        <p class="contact__name"><span class="contact__first">Jonas</span> <span class="contact__last">Berger</span></p>
        <p class="contact__line">+49 171 2846 530</p>
        <p class="contact__line">info@glutmeister.de</p>
        <p class="contact__line">www.glutmeister.de</p>
        <p class="contact__line">Instagram: @glutmeister.bbq</p>
      </div>
    </div>
    <div class="panel panel--black">
      <div class="wordmark">
        <span class="wordmark__dot"></span>
        <span class="wordmark__name">Glutmeister</span>
      </div>
    </div>
  </section>

  <section class="spread spread--inside" aria-label="Innenseite">
    <div class="panel panel--charcoal">
      <div class="badge" role="img" aria-label="Siegel des Fleischsommeliers"></div>
    </div>
    <div class="panel panel--black">
      <div class="photo" role="img" aria-label="Schwarzweißfoto des Fleischsommeliers mit Brille"></div>
      <div class="tagline">
        <p class="tagline__line">Fleisch mit Herkunft</p>
        <p class="tagline__line">Handwerk seit 1987</p>
        <p class="tagline__line">Grillkurse und Beratung</p>
      </div>
    </div>
  </section>
</body>
</html>
```